Business card and insta posting square

This is for 2 separate projects...

1...a double sided business card for online business (no address) to hand to businesses to get them to list their details on my online directory. the butterfly logo is to be used on the business card.

2.... a posting square for Instagram to write inspirational quotes over the top of to post....with a small butterfly logo somewhere on it (in a corner maybe)....the square is to have a thin, solid green outline around the edge of it, and a faded picture through the background that will allow me to write text over the top of it that will be easily readable.
I would like the same box for all Instagram quote posts for consistency ..

Target Market(s)

spiritual , yoga, meditation, wellness......

Industry/Entity Type

Wellness

Contact Information for Business Card

Details for Business Card...
Wandering The Quiet Tide
Your Complete Wellness Directory
www.wanderingthequiettide.example
insta/FB/pinterest/twitter
*List Your Business for FREE *

Colors
33b8a4
34a7d8
3276b5
876aae
9bcb3c

Requirements
Must have
• butterfly logo included on business card
• insta post square can use the butterfly logo OR the WTQT green square uploaded in the images
Nice to have
• greens

```html
<!DOCTYPE html>
<html lang="en">
<head>
<meta charset="utf-8">
<title>Wandering The Quiet Tide – Business Card</title>
<link href="https://fonts.googleapis.com/css2?family=Montserrat:ital,wght@0,600;0,700;1,700&family=Oswald:wght@500&family=Roboto:wght@300&display=swap" rel="stylesheet">
<style>
  :root{
    --bg:#e9e9e7;
    --card:#ffffff;
    --green:#3f9a3a;
    --green-dark:#1f7a3a;
    --badge:#4cae4c;
    --rule:#34a7d8;
    --purple:#4b2a7a;
    --fb:#3b5998;
    --pin:#cc1d24;
    --insta:#c0265a;
    --tw:#55a7e0;
    --gold:#f1c43e;
    --list:#4a5fa8;
    --faint:#cdc3e6;
  }
  *{box-sizing:border-box;margin:0;padding:0}
  html,body{width:1200px;height:1000px;overflow:hidden}
  body{background:var(--bg);position:relative;font-family:"Montserrat",sans-serif}
  .card{
    position:absolute;width:660px;height:430px;background:var(--card);
    border-radius:22px;box-shadow:0 6px 18px rgba(0,0,0,.18);
  }
  .card--front{left:440px;top:40px}
  .card--back{left:100px;top:520px}

  .badge{position:absolute;left:22px;top:20px;display:flex;align-items:center;gap:8px}
  .badge__dot{width:40px;height:40px;border-radius:50%;background:var(--badge)}
  .badge__name{font-family:"Montserrat",sans-serif;font-weight:700;font-size:15px;color:var(--badge)}

  .logo-mark{
    position:absolute;left:250px;top:28px;width:200px;height:170px;border-radius:10px;
    background:linear-gradient(150deg,#33b8a4 0%,#3276b5 45%,#876aae 100%);
  }
  .brand-name{
    position:absolute;left:0;right:0;top:205px;text-align:center;
    font-family:"Oswald",sans-serif;font-weight:500;font-size:40px;color:var(--green);letter-spacing:1px;
  }
  .rule{position:absolute;left:92px;right:60px;top:270px;height:3px;background:var(--rule)}

  .social{position:absolute;font-weight:700;font-size:14px;display:flex;align-items:center;gap:9px}
  .social__icon{width:14px;height:14px;border-radius:3px}
  .social--fb{left:160px;top:283px;color:var(--fb)} .social--fb .social__icon{background:var(--fb)}
  .social--pin{left:150px;top:312px;color:var(--pin)} .social--pin .social__icon{background:var(--pin);border-radius:50%}
  .social--insta{left:420px;top:312px;color:var(--insta)} .social--insta .social__icon{background:var(--insta)}
  .social--tw{left:415px;top:342px;color:var(--tw)} .social--tw .social__icon{background:var(--tw);border-radius:50%}
  .social--web{left:235px;top:360px;color:var(--purple)}

  .flutter{position:absolute;width:46px;height:46px;border-radius:50%;
    background:radial-gradient(circle,var(--faint) 0%,rgba(205,195,230,0) 72%)}
  .flutter--fl{left:44px;top:290px} .flutter--fr{right:30px;top:350px}
  .flutter--bl{left:70px;top:30px} .flutter--br{right:40px;top:95px}

  .title-box{
    position:absolute;left:150px;top:38px;width:420px;height:92px;
    border:4px solid var(--gold);
    background:linear-gradient(90deg,#eef6ee,#f8fbf6 50%,#eef6ee);
    text-align:center;padding-top:10px;
  }
  .title-box__name{font-family:"Oswald",sans-serif;font-weight:500;font-size:26px;letter-spacing:4px;color:var(--green-dark)}
  .title-box__tag{font-family:"Oswald",sans-serif;font-weight:500;font-size:16px;letter-spacing:.5px;color:var(--green-dark);margin-top:2px}

  .cta{
    position:absolute;left:115px;top:345px;
    font-family:"Roboto",sans-serif;font-weight:300;font-size:30px;color:var(--list);
    text-decoration:underline;text-underline-offset:4px;
  }
</style>
</head>
<body>
  <section class="card card--front" aria-label="Business card front">
    <div class="badge"><span class="badge__dot"></span><span class="badge__name">WTQT</span></div>
    <div class="logo-mark" role="img" aria-label="Butterfly logo mark with small butterflies rising"></div>
    <h1 class="brand-name">Wandering The Quiet Tide</h1>
    <div class="rule"></div>
    <span class="flutter flutter--fl" role="img" aria-label="Faint butterfly decoration"></span>
    <span class="flutter flutter--fr" role="img" aria-label="Faint butterfly decoration"></span>
    <p class="social social--fb"><span class="social__icon"></span>www.friendwall.example</p>
    <p class="social social--pin"><span class="social__icon"></span>www.pinboard.example</p>
    <p class="social social--insta"><span class="social__icon"></span>www.photostream.example</p>
    <p class="social social--tw"><span class="social__icon"></span>www.chirpline.example</p>
    <p class="social social--web">
      <svg width="16" height="16" viewBox="0 0 16 16" aria-hidden="true"><g fill="none" stroke="#333" stroke-width="1.4"><circle cx="8" cy="8" r="6.5"/><ellipse cx="8" cy="8" rx="3" ry="6.5"/><line x1="1.5" y1="8" x2="14.5" y2="8"/></g></svg>
      www.wanderingthequiettide.example
    </p>
  </section>

  <section class="card card--back" aria-label="Business card back">
    <span class="flutter flutter--bl" role="img" aria-label="Faint butterfly decoration"></span>
    <span class="flutter flutter--br" role="img" aria-label="Faint butterfly decoration"></span>
    <div class="title-box">
      <p class="title-box__name">WANDERING THE QUIET TIDE</p>
      <p class="title-box__tag">YOUR COMPLETE WELLNESS DIRECTORY</p>
    </div>
    <p class="cta">*LIST YOUR BUSINESS FOR FREE*</p>
  </section>
</body>
</html>
```